Quarrytide Hosting - Direct Mailer / Flyer

We are excited to announce the launch of our new company, Quarrytide Hosting, a premier cohosting facility and data center dedicated to Cryptocurrency Miners. Our website, https://quarrytidehosting.example, provides detailed information about our offerings and showcases the innovative design schemes for the entire project.

Quarrytide Hosting stands out in the industry by offering both GPU Hosting and ASIC Hosting services in our state-of-the-art facility, equipped with an impressive 17 Megawatts of available power. What sets us apart is our unique billing system based on actual metered power usage. We charge $0.08 for ASIC miners and $0.09 for GPU miners, ensuring cost-effectiveness and transparency for our clients.

Our commitment to excellence is evident in our use of cutting-edge technology, top-notch facilities, and strategic partnerships. These elements come together to deliver exceptional solutions tailored for real-world applications in the cryptocurrency space.

As part of our promotional efforts, we are developing a direct mailer/flyer to introduce Quarrytide Hosting to a wider audience. This promotional material will also serve as a handout at events, to potential customers, and more. We welcome creative ideas and suggestions to maximize the versatility of this design and reach diverse target audiences effectively.

For a comprehensive overview of our services and to explore our design concepts, please visit https://quarrytidehosting.example. Quarrytide Hosting is poised to revolutionize the mining industry, and we look forward to partnering with you for success in the digital currency era.

```html
<!DOCTYPE html>
<html lang="en">
<head>
<meta charset="utf-8">
<title>Quarrytide Hosting – Flyer</title>
<link href="https://fonts.googleapis.com/css2?family=Poppins:wght@400;500&family=Space+Grotesk:wght@500;700&display=swap" rel="stylesheet">
<style>
:root{
  --blue:#3a56fb;
  --mist:#e4ece8;
  --ink:#1f1f24;
  --white:#ffffff;
  --canvas:#ffffff;
}
*{box-sizing:border-box;margin:0;padding:0}
html,body{width:1200px;height:791px;overflow:hidden;background:var(--canvas)}
body{position:relative;font-family:"Poppins",sans-serif;color:var(--ink)}
.page{position:absolute;top:38px;width:544px;height:703px;background:var(--white);overflow:hidden;box-shadow:0 1px 4px rgba(0,0,0,.12)}
.page--front{left:41px}
.page--back{left:617px}
.page-bg{position:absolute;inset:0}
.heading{font-family:"Space Grotesk",sans-serif;font-weight:500;color:var(--blue);position:absolute;white-space:nowrap}
.wordmark{position:absolute;display:flex;align-items:center;gap:10px;font-family:"Space Grotesk",sans-serif;font-weight:700;color:var(--ink);text-transform:uppercase;white-space:nowrap}
.wordmark__mark{background:var(--ink);display:block}
.wordmark--large{left:40px;top:83px;font-size:41px;letter-spacing:1px}
.wordmark--large .wordmark__mark{width:50px;height:47px;border-radius:3px}
.wordmark--small{right:68px;top:24px;font-size:19px}
.wordmark--small .wordmark__mark{width:22px;height:22px;border-radius:2px}
.banner-title{position:absolute;left:185px;top:159px;font-family:"Space Grotesk",sans-serif;font-weight:500;font-size:22.5px;color:var(--white);white-space:nowrap}
.feature{position:absolute;display:flex;align-items:center;font-size:10.8px;font-weight:500;text-transform:uppercase;letter-spacing:.2px;white-space:nowrap}
.icon{width:30px;height:30px;background:var(--blue);border-radius:2px;display:flex;align-items:center;justify-content:center;flex:none}
.icon svg{width:21px;height:21px;fill:none;stroke:var(--white);stroke-width:1.3;stroke-linecap:round;stroke-linejoin:round}
.feature .icon{margin-right:18px}
.body-text{position:absolute;font-size:10.6px;line-height:23px;width:225px}
.footer{position:absolute;left:0;bottom:0;width:544px;height:40px;background:var(--blue);color:var(--white);font-size:10.4px;font-weight:500;text-align:center;line-height:38px;letter-spacing:.2px}
.photo{position:absolute;inset:0}
.cta-title{position:absolute;left:30px;top:506px;font-family:"Space Grotesk",sans-serif;font-weight:500;font-size:18.5px;color:var(--blue);white-space:nowrap}
.cta-button{position:absolute;left:398px;top:505px;width:116px;height:32px;border-radius:16px;background:var(--blue);color:var(--white);font-size:13px;font-weight:500;display:flex;align-items:center;justify-content:center;letter-spacing:.3px}
.contact-band{position:absolute;left:0;top:565px;width:544px;height:138px;background:var(--blue);color:var(--white)}
.contact-title{position:absolute;width:100%;top:28px;text-align:center;font-family:"Space Grotesk",sans-serif;font-weight:500;font-size:18px}
.contact{position:absolute;top:72px;display:flex;align-items:center}
.contact .icon{background:var(--white);margin-right:16px}
.contact .icon svg{stroke:var(--blue)}
.contact__text{font-size:7.6px;font-weight:500;line-height:17px;text-transform:uppercase;letter-spacing:.2px;white-space:nowrap}
</style>
</head>
<body>

<!-- Front page -->
<section class="page page--front">
  <svg class="page-bg" width="544" height="703" viewBox="0 0 544 703" aria-hidden="true">
    <polygon points="0,0 544,0 544,139 190,139 0,282" fill="var(--mist)"/>
    <polygon points="190,139 544,139 544,206 103,206" fill="var(--blue)"/>
  </svg>

  <div class="wordmark wordmark--large"><span class="wordmark__mark"></span>Quarrytide Hosting</div>
  <h1 class="banner-title">Hosting Tailored To Your Needs</h1>

  <div class="feature" style="left:90px;top:253px"><span class="icon"><svg viewBox="0 0 24 24"><circle cx="11" cy="11" r="8"/><path d="M11 6v5l3 2"/><circle cx="18" cy="18" r="3.5"/></svg></span>99.45% Uptime</div>
  <div class="feature" style="left:90px;top:301px"><span class="icon"><svg viewBox="0 0 24 24"><rect x="3" y="12" width="18" height="7"/><circle cx="7" cy="19" r="1.5"/><circle cx="12" cy="19" r="1.5"/><circle cx="17" cy="19" r="1.5"/><path d="M6 12V5M4 7l2-2 2 2M11 12V8h5v4"/></svg></span>Large Facility Capacity</div>
  <div class="feature" style="left:90px;top:349px"><span class="icon"><svg viewBox="0 0 24 24"><ellipse cx="10" cy="5" rx="6" ry="2.5"/><path d="M4 5v12c0 1.4 2.7 2.5 6 2.5M16 5v6"/><path d="M4 11c0 1.4 2.7 2.5 6 2.5"/><circle cx="17" cy="17" r="4.5"/><path d="M17 15v2l1.5 1"/></svg></span>Metered Usage</div>

  <div class="feature" style="left:308px;top:253px"><span class="icon"><svg viewBox="0 0 24 24"><path d="M12 3l7 3v6c0 4-3 7-7 9-4-2-7-5-7-9V6z"/><path d="M8.5 12l2.5 2.5 4.5-5"/></svg></span>Advanced Security</div>
  <div class="feature" style="left:308px;top:301px"><span class="icon"><svg viewBox="0 0 24 24"><circle cx="10" cy="9" r="4"/><path d="M3 21c0-4 3-6 7-6s7 2 7 6z"/><rect x="15" y="2" width="7" height="5" rx="1"/></svg></span>Expert Support</div>
  <div class="feature" style="left:308px;top:349px"><span class="icon"><svg viewBox="0 0 24 24"><rect x="3" y="6" width="13" height="10"/><path d="M2 19h15"/><rect x="16" y="3" width="5" height="13" rx="1"/><circle cx="9.5" cy="11" r="2.5"/></svg></span>Direct Equipment Access</div>

  <h2 class="heading" style="left:44px;top:414px;font-size:22px">About Company</h2>
  <p class="body-text" style="left:44px;top:458px">Quarrytide Hosting has committed to leveraging cutting-edge technology, state-of-the-art facilities, and strategic partnerships to deliver exceptional solutions tailored for real-world applications in the cryptocurrency space.</p>
  <p class="body-text" style="left:298px;top:458px;width:205px">Transform Mining With Cohosting Miners deserve the best - choose the hosting company that delivers excellence! Embark on your Hosting Journey with rates starting at $0.09 kWh, all-in for GPU Miners, welcoming all equipment.</p>

  <footer class="footer">ALL RIGHTS RESERVED. 2024 © QUARRYTIDE GROUP, LLC.</footer>
</section>

<!-- Back page -->
<section class="page page--back">
  <svg class="page-bg" width="544" height="703" viewBox="0 0 544 703" aria-hidden="true">
    <polygon points="0,474 351,474 544,335 544,565 0,565" fill="var(--mist)"/>
  </svg>
  <svg class="photo" width="544" height="703" viewBox="0 0 544 703" role="img" aria-label="Photograph of stacked gold and silver cryptocurrency coins over a trading chart">
    <defs>
      <linearGradient id="coins" x1="0" y1="1" x2="1" y2="0">
        <stop offset="0" stop-color="#c9922f"/>
        <stop offset=".45" stop-color="#b98a45"/>
        <stop offset=".7" stop-color="#3d5570"/>
        <stop offset="1" stop-color="#c7c9cc"/>
      </linearGradient>
    </defs>
    <path d="M520,12 Q530,8 544,8 L544,335 L386,458 Q372,468 361,455 L254,318 Q242,300 255,285 Z" fill="url(#coins)"/>
  </svg>

  <div class="wordmark wordmark--small"><span class="wordmark__mark"></span>Quarrytide Hosting</div>

  <h2 class="heading" style="left:43px;top:75px;font-size:22px">Our Solutions</h2>
  <p class="body-text" style="left:44px;top:118px;width:236px">Tailored Hosting Solutions For Every Individuals Need Quarrytide Hosting has committed to leveraging cutting-edge technology, state-of-the-art facilities, and strategic partnerships to deliver exceptional solutions tailored for real-world applications in the cryptocurrency space.</p>

  <div class="feature" style="left:44px;top:296px"><span class="icon"><svg viewBox="0 0 24 24"><path d="M7 11a4 4 0 010-8 5 5 0 019 1 3.5 3.5 0 011 7z"/><rect x="7" y="12" width="10" height="5"/><path d="M9 17v4M12 17v4M15 17v4"/></svg></span>GPU Hosting</div>
  <div class="feature" style="left:44px;top:339px"><span class="icon"><svg viewBox="0 0 24 24"><rect x="3" y="3" width="15" height="5"/><rect x="3" y="9" width="15" height="5"/><rect x="3" y="15" width="10" height="5"/><path d="M17 15l3 1v2.5c0 1.5-1.3 2.5-3 3-1.7-.5-3-1.5-3-3V16z"/></svg></span>ASIC Hosting</div>
  <div class="feature" style="left:44px;top:382px"><span class="icon"><svg viewBox="0 0 24 24"><rect x="5" y="5" width="14" height="14"/><rect x="9" y="9" width="6" height="6"/><path d="M9 2v3M12 2v3M15 2v3M9 19v3M12 19v3M15 19v3M2 9h3M2 12h3M2 15h3M19 9h3M19 12h3M19 15h3"/></svg></span>Mining Hardware</div>
  <div class="feature" style="left:44px;top:425px"><span class="icon"><svg viewBox="0 0 24 24"><circle cx="9" cy="8" r="3"/><path d="M4 17c0-3 2-5 5-5s5 2 5 5"/><path d="M3 17h16M5 17v4M17 17v4"/><rect x="14" y="3" width="7" height="5" rx="1"/></svg></span>Crypto Consulting</div>

  <p class="cta-title">Your Mining Success Story Begins Here</p>
  <a class="cta-button">GET STARTED</a>

  <div class="contact-band">
    <h3 class="contact-title">Have Questions? Contact Us For Expert Advice</h3>
    <div class="contact" style="left:39px"><span class="icon"><svg viewBox="0 0 24 24"><path d="M4 5h13v9H9l-4 3v-3H4z"/><path d="M7 8h7M7 11h5"/></svg></span><div class="contact__text">Chat Us<br>Live Chat</div></div>
    <div class="contact" style="left:182px"><span class="icon"><svg viewBox="0 0 24 24"><rect x="3" y="6" width="18" height="12"/><path d="M3 6l9 7 9-7"/></svg></span><div class="contact__text">Email Us<br>hello@quarrytidehosting.example</div></div>
    <div class="contact" style="left:384px"><span class="icon"><svg viewBox="0 0 24 24"><path d="M6 3l3 4-2 2a11 11 0 008 8l2-2 4 3-2 3C10 21 3 14 3 5z"/></svg></span><div class="contact__text">Schedule 1-on-1<br>Interact With Us</div></div>
  </div>
</section>

</body>
</html>
```